Luxury Lifestyle Website - Blog and Product Showcasing

I am looking to create a simple, yet elegant website where I can post blog posts and feature products and brand partnerships for my company, Velmora Haus. I want a very elegant but not overly complex site. I like the look and feel of Corinne Ashdale's site - I don't need for it to be that robust or sophisticated, but that is the aesthetic I am going for. I would like to include my primary logo at the top of the main page, and also incorporate my alternative logos throughout the site in strategic places.

Target Market(s)

Luxury Brands; 20s-60s year olds; women; high-end fashion and tastes

Industry/Entity Type

Luxury Lifestyle - Blogging - Product Showcasing

Coding

Coded - Design and coding required

Number of Pages Required

4 page

Font styles to use
Sans Serif
Script
Other font styles liked:
• Pinyon

Colors
00AB8E
00BBA5
67D7C9
C6EFE9
E9F9F6
59FF00
82FF00
B8FF75
E3FFCB
F4FFEA

Requirements
Must have
• Creative use of my various logos. PASTEL GREENS or a DEEP DARK GREEN. Nothing bright, very soft and elegant.
Nice to have
• Elegant script that is easy to read.
Should not have
• Bright colors or overly modern look or feel.

```html
<!DOCTYPE html>
<html lang="en">
<head>
<meta charset="utf-8">
<title>Velmora Haus</title>
<link href="https://fonts.googleapis.com/css2?family=Pinyon+Script&family=Roboto:wght@400;500;700&display=swap" rel="stylesheet">
<style>
:root{
  --teal:#00BBA5;
  --teal-deep:#00AB8E;
  --mint:#E9F9F6;
  --mint-mid:#C6EFE9;
  --ink:#222222;
  --text:#444444;
  --footer:#1d1d1d;
  --footer-text:#cfcfcf;
  --white:#ffffff;
}
*{margin:0;padding:0;box-sizing:border-box}
html,body{width:1200px;height:4028px;overflow:hidden}
body{font-family:'Roboto',Arial,sans-serif;color:var(--text);background:var(--white);position:relative}
.script{font-family:'Pinyon Script',cursive;color:var(--ink);font-weight:400}
.btn{display:inline-flex;align-items:center;gap:10px;background:var(--teal);color:var(--white);font-size:15px;font-weight:700;text-transform:uppercase;letter-spacing:.5px;padding:0 28px;height:42px;border-radius:21px;text-decoration:none}
.btn svg{width:14px;height:14px}
.photo{display:block}

/* header + hero */
.hero{position:absolute;top:0;left:0;width:1200px;height:780px;background:linear-gradient(135deg,#a67a5c 0%,#c79a78 35%,#8a6a58 65%,#5e4a42 100%)}
.topbar{position:absolute;top:0;left:0;width:1200px;height:78px;background:var(--white)}
.nav{position:absolute;top:30px;font-size:15px;font-weight:500;color:var(--ink);letter-spacing:.5px}
.brand{position:absolute;left:480px;top:0;width:240px;height:150px;background:var(--white);border-radius:0 0 120px 120px;display:flex;flex-direction:column;align-items:center;justify-content:center;gap:10px}
.brand .mark{width:34px;height:34px;border:2px solid #6b6b6b}
.brand .name{font-size:20px;font-weight:500;letter-spacing:3px;color:#5a5a5a;text-transform:uppercase}
.hero-title{position:absolute;top:385px;left:0;width:1200px;text-align:center;color:var(--white);font-size:58px;line-height:84px}
.hero .btn{position:absolute;left:527px;top:558px;height:42px}

/* services */
.section-title{position:absolute;width:1200px;left:0;text-align:center;font-size:44px}
.card{position:absolute;top:928px;width:288px}
.card .photo{width:288px;height:296px}
.card h3{margin-top:22px;text-align:center;font-size:17px;font-weight:700;color:var(--ink)}
.card a{display:block;text-align:center;margin-top:10px;font-size:16px;color:var(--teal);font-weight:500;text-decoration:underline}

/* about */
.about{position:absolute;top:1380px;left:0;width:1200px;height:492px;background:var(--mint)}
.about .photo{position:absolute;left:0;top:0;width:600px;height:492px;background:linear-gradient(160deg,#c9b59a,#6e6a5a 55%,#2d3a33)}
.about-body{position:absolute;left:686px;top:46px;width:440px}
.about-body h2{font-size:44px;margin-bottom:10px}
.about-body p{font-size:15px;line-height:20px;color:var(--text)}
.about-body .btn{margin-top:22px}

/* spotlight */
.spot-title{top:1950px}
.spot-text{position:absolute;top:2020px;left:150px;width:900px;text-align:center;font-size:15px;line-height:22px}
.spot .btn{position:absolute;left:513px;top:2180px}

/* shop */
.shop{position:absolute;top:2312px;left:0;width:1200px;height:448px;background:var(--mint)}
.product{position:absolute;top:156px;width:140px;text-align:center}
.product .photo{width:140px;height:160px;margin:0 auto}
.product .btn{margin-top:34px;border-radius:2px;height:36px;font-size:14px;text-transform:none;padding:0 24px}

/* strip */
.strip .photo{position:absolute;top:2760px;height:400px}

/* gallery */
.gallery .photo{position:absolute;top:3312px;width:196px;height:208px}

/* footer */
.footer{position:absolute;top:3620px;left:0;width:1200px;height:408px;background:var(--footer);color:var(--footer-text)}
.f-brand{position:absolute;left:110px;top:96px;width:270px;text-align:center}
.f-brand .name{font-size:28px;letter-spacing:4px;text-transform:uppercase;color:#9a9a9a;font-weight:500}
.f-brand .tag{margin-top:6px;font-size:11px;letter-spacing:3px;color:#9a9a9a}
.socials{display:flex;gap:12px;justify-content:center;margin-top:26px}
.socials span{width:30px;height:30px;border:1.5px solid #bdbdbd;border-radius:50%}
.f-col{position:absolute;top:78px}
.f-col h4{font-size:16px;color:var(--white);font-weight:700;margin-bottom:18px}
.f-col li{list-style:none;font-size:13px;line-height:24px}
.contact-item{display:flex;gap:12px;margin-bottom:14px}
.contact-item svg{width:16px;height:16px;flex:none;margin-top:2px}
.contact-item b{display:block;color:var(--white);font-size:13px;font-weight:700;line-height:18px}
.contact-item span{font-size:13px;line-height:18px}
.copy{position:absolute;top:360px;left:0;width:1200px;text-align:center;font-size:13px;color:var(--footer-text)}
.to-top{position:absolute;right:30px;top:330px;width:38px;height:38px;border-radius:50%;background:var(--teal-deep);display:flex;align-items:center;justify-content:center}
</style>
</head>
<body>

<header class="hero">
  <div class="photo" role="img" aria-label="Woman in a wide-brimmed hat and camel coat smiling above old town rooftops" style="width:1200px;height:780px;background:linear-gradient(135deg,#a67a5c 0%,#c79a78 35%,#8a6a58 65%,#5e4a42 100%)"></div>
  <div class="topbar"></div>
  <nav>
    <span class="nav" style="left:190px">HOME</span>
    <span class="nav" style="left:280px">ABOUT US</span>
    <span class="nav" style="left:396px">SERVICES</span>
    <span class="nav" style="left:758px">SHOP</span>
    <span class="nav" style="left:844px">TESTIMONIALS</span>
    <span class="nav" style="left:994px">CONTACT US</span>
  </nav>
  <div class="brand"><span class="mark"></span><span class="name">Velmora Haus</span></div>
  <h1 class="hero-title script">The Authority on Living an Elegantly<br>Extravagant Existence</h1>
  <a class="btn" href="#">Get Started
    <svg viewBox="0 0 14 14"><circle cx="7" cy="7" r="7" fill="#fff"/><path d="M5.5 4l3 3-3 3" stroke="#00BBA5" stroke-width="1.8" fill="none"/></svg></a>
</header>

<section class="services">
  <h2 class="section-title script" style="top:840px">Our Services</h2>
  <article class="card" style="left:136px">
    <div class="photo" role="img" aria-label="Woman in a pale blue ruffled dress outdoors" style="background:linear-gradient(160deg,#d8c9b0,#9fb6c4 60%,#7c8f8a)"></div>
    <h3>Lorem ipsum dolor sit amet</h3><a href="#">Read More</a>
  </article>
  <article class="card" style="left:456px">
    <div class="photo" role="img" aria-label="Woman in a light trench coat on a city street" style="background:linear-gradient(160deg,#c7b9a6,#d9d2c6 50%,#8c7a68)"></div>
    <h3>Lorem ipsum dolor sit amet</h3><a href="#">Read More</a>
  </article>
  <article class="card" style="left:776px">
    <div class="photo" role="img" aria-label="Woman in a long silver gown" style="background:linear-gradient(160deg,#6d6a6e,#9a98a8 55%,#4d4b55)"></div>
    <h3>Lorem ipsum dolor sit amet</h3><a href="#">Read More</a>
  </article>
</section>

<section class="about">
  <div class="photo" role="img" aria-label="Woman in a black dress and sunglasses on a sunny street"></div>
  <div class="about-body">
    <h2 class="script">About Us</h2>
    <p>Lorem ipsum dolor sit amet, consectetur adipiscing elit, sed do eiusmod tempor incididunt ut labore et dolore magna aliqua. Ut enim ad minim veniam, quis nostrud exercitation ullamco laboris nisi ut aliquip ex ea commodo consequat. Duis aute irure dolor in reprehenderit in voluptate velit esse cillum dolore eu fugiat nulla pariatur. Excepteur sint occaecat cupidatat non proident, sunt in culpa qui officia deserunt mollit anim id est laborum. Lorem ipsum dolor sit amet, consectetur adipiscing elit, sed do eiusmod tempor incididunt ut labore et dolore magna aliqua enim ad minim veniam, quis nostrud exercitation ullamco laboris nisi aliquip ex ea commodo consequat.</p>
    <a class="btn" href="#">Learn More
      <svg viewBox="0 0 14 14"><circle cx="7" cy="7" r="7" fill="#fff"/><path d="M5.5 4l3 3-3 3" stroke="#00BBA5" stroke-width="1.8" fill="none"/></svg></a>
  </div>
</section>

<section class="spot">
  <h2 class="section-title script spot-title">In The Spotlight... Tan Leather Ballet Flats</h2>
  <p class="spot-text">Lorem ipsum dolor sit amet, consectetur adipiscing elit, sed do eiusmod tempor incididunt ut labore et dolore magna aliqua. Ut enim ad minim veniam, quis nostrud exercitation ullamco laboris nisi ut aliquip ex ea commodo consequat. Duis aute irure dolor in reprehenderit in voluptate velit esse cillum dolore eu fugiat nulla pariatur. Excepteur sint occaecat cupidatat non proident, sunt in culpa qui officia deserunt mollit anim id est laborum. Lorem ipsum dolor sit amet, consectetur adipiscing elit, sed do eiusmod tempor incididunt ut labore et dolore magna aliqua. Ut enim ad minim veniam, quis nostrud exercitation.</p>
  <a class="btn" href="#">Learn More
    <svg viewBox="0 0 14 14"><circle cx="7" cy="7" r="7" fill="#fff"/><path d="M5.5 4l3 3-3 3" stroke="#00BBA5" stroke-width="1.8" fill="none"/></svg></a>
</section>

<section class="shop">
  <h2 class="section-title script" style="top:64px">Our Shop</h2>
  <div class="product" style="left:120px">
    <div class="photo" role="img" aria-label="Yellow floral sundress" style="background:linear-gradient(180deg,#f2cf5c,#e2a93a)"></div>
    <a class="btn" href="#">Shop Now</a>
  </div>
  <div class="product" style="left:390px">
    <div class="photo" role="img" aria-label="Navy sleeveless dress" style="background:linear-gradient(180deg,#2c3d7a,#1b2758)"></div>
    <a class="btn" href="#">Shop Now</a>
  </div>
  <div class="product" style="left:660px">
    <div class="photo" role="img" aria-label="Periwinkle shirt dress" style="background:linear-gradient(180deg,#8b96d6,#6670b8)"></div>
    <a class="btn" href="#">Shop Now</a>
  </div>
  <div class="product" style="left:930px">
    <div class="photo" role="img" aria-label="Red fitted dress" style="background:linear-gradient(180deg,#e6343a,#b81e25)"></div>
    <a class="btn" href="#">Shop Now</a>
  </div>
</section>

<section class="strip">
  <div class="photo" role="img" aria-label="Woman in a black blazer with gold earrings" style="left:0;width:378px;background:linear-gradient(160deg,#c9b39c,#5a4a40 60%,#1f1c1c)"></div>
  <div class="photo" role="img" aria-label="Video still of a woman in a rust coat and sunglasses on a street" style="left:382px;width:398px;background:linear-gradient(160deg,#d9cbb8,#a56a3f 55%,#5b4436)"></div>
  <svg style="position:absolute;left:555px;top:2925px;width:50px;height:50px" viewBox="0 0 50 50"><circle cx="25" cy="25" r="24" fill="#fff" opacity=".9"/><path d="M20 15l14 10-14 10z" fill="#333"/></svg>
  <div class="photo" role="img" aria-label="Bride holding a white and green bouquet" style="left:784px;width:416px;background:linear-gradient(160deg,#efe9df,#c9c4b4 55%,#8b8f74)"></div>
</section>

<section class="gallery">
  <h2 class="section-title script" style="top:3222px">Our Gallery</h2>
  <div class="photo" role="img" aria-label="Woman in a dark hat and coat" style="left:100px;background:linear-gradient(160deg,#bfb6ad,#5d524c)"></div>
  <div class="photo" role="img" aria-label="Woman seated in a neutral outfit" style="left:302px;background:linear-gradient(160deg,#e0d7cc,#9a8a78)"></div>
  <div class="photo" role="img" aria-label="Woman in a camel coat on a street" style="left:504px;background:linear-gradient(160deg,#d2c2b0,#9b7a5e)"></div>
  <div class="photo" role="img" aria-label="Woman in a rust jacket against blue sky" style="left:706px;background:linear-gradient(160deg,#6aa0cf,#c7743e)"></div>
  <div class="photo" role="img" aria-label="Woman in a light knit sweater" style="left:908px;background:linear-gradient(160deg,#b9c7d6,#e6e1da)"></div>
</section>

<footer class="footer">
  <div class="f-brand">
    <div class="name">Velmora Haus</div>
    <div class="tag">LUXURY LIFESTYLE</div>
    <div class="socials"><span></span><span></span><span></span><span></span></div>
  </div>
  <div class="f-col" style="left:470px">
    <h4>Quick Links</h4>
    <ul><li>Home</li><li>About Us</li><li>Services</li><li>Shop</li><li>Testimonials</li><li>Contact Us</li></ul>
  </div>
  <div class="f-col" style="left:692px">
    <h4>Other Links</h4>
    <ul><li>Legal Information</li><li>Terms &amp; Condition</li><li>Privacy Policy</li><li>Support</li><li>Site Map</li></ul>
  </div>
  <div class="f-col" style="left:892px;width:240px">
    <h4>Contact Us</h4>
    <div class="contact-item">
      <svg viewBox="0 0 16 16"><path d="M3 1h3l1.5 4-2 1.2a9 9 0 004.3 4.3L11 8.5l4 1.5v3a2 2 0 01-2 2A13 13 0 011 3a2 2 0 012-2z" fill="#00BBA5"/></svg>
      <div><b>Phone</b><span>+1 555 014 2280</span></div>
    </div>
    <div class="contact-item">
      <svg viewBox="0 0 16 16"><rect x="1" y="3" width="14" height="10" rx="1" fill="#00BBA5"/><path d="M1.5 3.5L8 9l6.5-5.5" stroke="#1d1d1d" stroke-width="1.3" fill="none"/></svg>
      <div><b>Email</b><span>info@velmorahaus.com</span></div>
    </div>
    <div class="contact-item">
      <svg viewBox="0 0 16 16"><path d="M8 1a5 5 0 015 5c0 4-5 9-5 9S3 10 3 6a5 5 0 015-5z" fill="#00BBA5"/><circle cx="8" cy="6" r="2" fill="#1d1d1d"/></svg>
      <div><b>Location</b><span>140 Lorem ipsum dolor sit<br>consectetur adipiscing elit,</span></div>
    </div>
  </div>
  <a class="to-top" href="#"><svg width="14" height="14" viewBox="0 0 14 14"><path d="M3 9l4-4 4 4" stroke="#fff" stroke-width="2" fill="none"/></svg></a>
  <p class="copy">2023 Copyright - Velmora Haus &nbsp;|&nbsp; All Rights Reserved</p>
</footer>

</body>
</html>
```